Paws and Meadows is a dog walking service that offers home boarding and pet taxi

I am looking for a eye catching A5 leaflet/flyer design for my dog walking business Paws and Meadows.

The flyer must have my company logo on it (jpeg), a picture of my van (jpeg) and a picture of dogs playing (jpegs 1-5).

The fonts must be easy to read. I am not set on any colour scheme but do like the idea of having a natural background. IE. Green grass and blue sky or some forest setting with green trees. If you don't like this idea or its hard to work with don't worry I am open minded so be creative and do what you thinks best.

I'll provide quick feedback to designs that i like and so we can work together.

The flyers must contain the following:

60 minute group and individual walks
GPS Tracked Walks
Home Boarding
Pet Taxi
Puppy/Pet visits

Offer: 50% off first weeks dogs walks with this flyer.

As well as containing my contact info:

07915382046
www.paws-and-meadows.co.uk
paws-and-meadows@mailbrook.co.uk

Chatterbook, Chirpline and Snapgallery logos must be present as well.

Thanks and Good luck!

Target Market(s)

ANYONE WHO NEEDS THEIR DOG WALKED OR LOOKED AFTER WHEN THEY ARE ON HOLIDAY

Industry/Entity Type

Business

Contact Information for Business Card

THE BUSINESS CARD MUST DISPLAY THE LOGO THAT HAS BEEN UPLOADED IN A FILE. IT MUST LOOK SHARP AND PROFESSIONAL. CONTAIN ALL CONTACT INFO AND HAVE SERVICES OFFERED. SEE PROJECT DESCRIPTION FOR FLYER.

Font styles to use
Serif
Sans Serif

Requirements
Must have
• SEE PROJECT DESCRIPTION
Nice to have
• IT WOULD BE NICE TO HAVE PHOTOS OF MY VAN AND DOGS PLAYING. I HAVE UPLOADED SOME PICS OF VAN TO BE USED AND THERE ARE PICS OF DOGS PLAYING THAT COULD BE USED.

```html
<!DOCTYPE html>
<html lang="en">
<head>
<meta charset="utf-8">
<title>Paws and Meadows – Dog Walking &amp; Pet Services Flyer</title>
<link rel="stylesheet" href="https://fonts.googleapis.com/css2?family=Baloo+2:wght@600;700;800&family=Oswald:wght@500;600&family=Poppins:wght@500;600&display=swap">
<style>
  :root {
    --page-bg: #dcdcdc;
    --sky-deep: #2f86dc;
    --sky-mid: #6fb4ee;
    --sky-haze: #d4e9f8;
    --grass-light: #a9d86a;
    --grass-mid: #5cae2c;
    --grass-deep: #3c8a1c;
    --orange: #f7a11a;
    --blue-outline: #1d68cf;
    --ink: #2a2a2a;
    --white: #ffffff;
  }
  * { box-sizing: border-box; margin: 0; padding: 0; }
  html, body {
    width: 1200px; height: 1200px; overflow: hidden;
    background: var(--page-bg);
  }
  .flyer {
    position: absolute; left: 200px; top: 35px;
    width: 800px; height: 1130px; overflow: hidden;
    box-shadow: 0 12px 30px rgba(0,0,0,.25);
  }
  .scenery {
    position: absolute; inset: 0;
    background:
      radial-gradient(ellipse 260px 120px at 560px 200px, rgba(255,255,255,.95), rgba(255,255,255,0) 70%),
      radial-gradient(ellipse 220px 90px at 200px 170px, rgba(255,255,255,.8), rgba(255,255,255,0) 70%),
      radial-gradient(ellipse 200px 110px at 740px 430px, rgba(255,255,255,.85), rgba(255,255,255,0) 70%),
      linear-gradient(180deg, var(--sky-deep) 0%, var(--sky-mid) 35%, var(--sky-haze) 64%, var(--grass-light) 72%, var(--grass-mid) 84%, var(--grass-deep) 100%);
  }

  /* Brand block */
  .brand {
    position: absolute; top: 150px; left: 0; right: 0;
    display: flex; flex-direction: column; align-items: center;
    padding-left: 120px;
  }
  .brand-name {
    display: flex; align-items: center; gap: 14px;
    font-family: "Poppins", sans-serif; font-weight: 600;
    font-size: 38px; color: var(--ink); letter-spacing: 1px;
  }
  .brand-mark {
    width: 30px; height: 30px; border-radius: 50%;
    border: 4px solid var(--orange);
  }
  .brand-tagline {
    display: flex; align-items: center; gap: 8px; margin-top: 2px;
    font-family: "Poppins", sans-serif; font-weight: 500;
    font-size: 12px; letter-spacing: 2px; color: var(--ink);
  }
  .brand-tagline::before, .brand-tagline::after {
    content: ""; width: 60px; height: 2px; background: var(--grass-deep);
  }

  /* Headline */
  .headline {
    position: absolute; top: 240px; left: 40px; width: 740px;
    font-family: "Baloo 2", sans-serif; font-weight: 800;
    line-height: .95; text-transform: uppercase;
  }
  .headline-main {
    display: block; font-size: 86px; color: var(--orange);
    -webkit-text-stroke: 3px var(--white); paint-order: stroke fill;
    text-shadow: 3px 4px 0 rgba(0,0,0,.18);
  }
  .headline-sub {
    display: block; padding-left: 40px; font-size: 86px; color: var(--white);
    -webkit-text-stroke: 6px var(--blue-outline); paint-order: stroke fill;
    text-shadow: 3px 4px 0 rgba(0,0,0,.15);
  }

  /* Services */
  .services {
    position: absolute; top: 468px; left: 110px; width: 360px;
    list-style: none;
    font-family: "Baloo 2", sans-serif; font-weight: 700;
    font-size: 29px; line-height: 34px; color: var(--white);
    text-shadow: 0 1px 3px rgba(20,60,120,.35);
  }
  .services li { position: relative; padding-left: 26px; margin-bottom: 4px; }
  .services li::before {
    content: ""; position: absolute; left: 0; top: 11px;
    width: 12px; height: 12px; border-radius: 50%; background: var(--orange);
  }

  /* Offer */
  .offer {
    position: absolute; top: 520px; left: 470px; width: 310px; height: 220px;
  }
  .offer svg { position: absolute; inset: 0; }
  .offer-text {
    position: absolute; inset: 0;
    display: flex; flex-direction: column; align-items: center; justify-content: center;
    text-align: center; font-family: "Oswald", sans-serif;
  }
  .offer-amount { font-size: 60px; font-weight: 600; color: var(--orange); line-height: 1; }
  .offer-detail { font-size: 24px; font-weight: 500; color: var(--ink); line-height: 1.15; margin-top: 4px; }

  /* Photo row */
  .gallery {
    position: absolute; top: 720px; left: 14px; right: 14px;
    display: flex; justify-content: space-between;
  }
  .gallery-photo {
    width: 184px; height: 184px; border-radius: 50%;
    border: 9px solid rgba(230,242,252,.85);
  }
  .photo-van { background: linear-gradient(160deg, #4a9de0 0%, #e9eef2 45%, #c9302c 65%, #3e6b2a 100%); }
  .photo-pair { background: linear-gradient(150deg, #9ccf5a 0%, #c89a52 45%, #2b2420 75%, #6aa83a 100%); }
  .photo-lawn { background: linear-gradient(170deg, #5ea632 0%, #c08a5a 40%, #e6e2da 60%, #4c9528 100%); }
  .photo-tree { background: linear-gradient(175deg, #f2f5f2 0%, #8fbf5a 35%, #8a7a60 60%, #3f8a22 100%); }

  /* Contact */
  .contact {
    position: absolute; top: 990px; left: 56px;
    list-style: none;
    font-family: "Poppins", sans-serif; font-weight: 500;
    font-size: 19px; line-height: 30px; color: var(--white);
    text-shadow: 0 1px 3px rgba(0,0,0,.35);
  }
  .contact li { display: flex; align-items: center; gap: 8px; }
  .contact svg { width: 15px; height: 15px; flex: none; }

  /* Social */
  .social {
    position: absolute; top: 975px; left: 470px; width: 290px;
    display: flex; flex-direction: column; align-items: center;
  }
  .social-title {
    font-family: "Oswald", sans-serif; font-weight: 600; font-size: 28px;
    color: var(--white); text-shadow: 0 1px 3px rgba(0,0,0,.35);
  }
  .social-links {
    margin-top: 8px; padding: 10px 14px;
    border: 2px solid var(--white); border-radius: 12px;
    display: flex; gap: 12px;
    font-family: "Poppins", sans-serif; font-weight: 600; font-size: 15px;
    color: var(--white); text-shadow: 0 1px 3px rgba(0,0,0,.35);
  }
</style>
</head>
<body>
  <main class="flyer">
    <div class="scenery" role="img" aria-label="Photo background of blue sky with white clouds above a green meadow where dogs run and play"></div>

    <header class="brand">
      <div class="brand-name"><span class="brand-mark"></span>PAWS AND MEADOWS</div>
      <div class="brand-tagline">DOG WALKING SERVICE</div>
    </header>

    <h1 class="headline">
      <span class="headline-main">Dog Walking &amp;</span>
      <span class="headline-sub">Pet Services</span>
    </h1>

    <ul class="services">
      <li>60 minute group and individual walks</li>
      <li>GPS Tracked Walks</li>
      <li>Home Boarding</li>
      <li>Pet Taxi</li>
      <li>Puppy/Pet visits</li>
    </ul>

    <aside class="offer">
      <svg viewBox="0 0 310 220" aria-hidden="true">
        <path d="M60 60 Q70 18 120 28 Q150 0 190 22 Q240 10 255 55 Q300 70 290 115 Q305 160 262 175 Q250 212 200 200 Q165 222 130 202 Q80 215 62 180 Q15 170 22 128 Q0 88 60 60 Z"
              fill="#ffffff" stroke="#f7a11a" stroke-width="7"/>
      </svg>
      <div class="offer-text">
        <span class="offer-amount">50% OFF</span>
        <span class="offer-detail">first weeks dogs<br>walks with this flyer</span>
      </div>
    </aside>

    <section class="gallery">
      <div class="gallery-photo photo-van" role="img" aria-label="Photo of the branded dog walking van parked outdoors"></div>
      <div class="gallery-photo photo-pair" role="img" aria-label="Photo of two dogs carrying a stick together"></div>
      <div class="gallery-photo photo-lawn" role="img" aria-label="Photo of greyhounds resting on a grass lawn"></div>
      <div class="gallery-photo photo-tree" role="img" aria-label="Photo of a dog lying in long grass beside a tree"></div>
    </section>

    <ul class="contact">
      <li>
        <svg viewBox="0 0 24 24" fill="#ffffff" aria-hidden="true"><path d="M6.6 10.8a15.1 15.1 0 0 0 6.6 6.6l2.2-2.2a1 1 0 0 1 1-.25 11.4 11.4 0 0 0 3.6.57 1 1 0 0 1 1 1V20a1 1 0 0 1-1 1A17 17 0 0 1 3 4a1 1 0 0 1 1-1h3.5a1 1 0 0 1 1 1c0 1.25.2 2.45.57 3.57a1 1 0 0 1-.25 1z"/></svg>
        07915382046
      </li>
      <li>
        <svg viewBox="0 0 24 24" fill="none" stroke="#ffffff" stroke-width="2" aria-hidden="true"><circle cx="12" cy="12" r="9"/><path d="M3 12h18M12 3c3 3.5 3 14.5 0 18M12 3c-3 3.5-3 14.5 0 18"/></svg>
        www.paws-and-meadows.co.uk
      </li>
      <li>
        <svg viewBox="0 0 24 24" fill="#ffffff" aria-hidden="true"><path d="M2 5h20v14H2z" fill="none" stroke="#ffffff" stroke-width="2"/><path d="M2 5l10 8 10-8" fill="none" stroke="#ffffff" stroke-width="2"/></svg>
        paws-and-meadows@mailbrook.co.uk
      </li>
    </ul>

    <section class="social">
      <span class="social-title">Follow us on</span>
      <div class="social-links">
        <span>Chatterbook</span>
        <span>Chirpline</span>
        <span>Snapgallery</span>
      </div>
    </section>
  </main>
</body>
</html>
```